Marta Business Card

My wife is going to start her own business with renting holiday appartments to tourists. She needs a design for a new business card... and a new web site.
Look at Stayvolt "Erholung auf dem Lindenwäldchen"

Target Market(s)

Give business card to prospects at any situation

Contact Information for Business Card

not sure what this means

Font styles to use
Script

Colors
fec41a
fee18a

Requirements
Must have
• My wife's handwriting is difficult to read:
Entspannen - Loslassen - Auftanken
Marta & das Lindenwäldchen
Urlaub an einem besonderen Ort
Marta Brecke
Grauer Pfad 7
18471 Alt Feldow
post@marta-brecke.de
www.lindenwaeldchen.net
Nice to have
• Beige background
Font like handwriting

```html
<!DOCTYPE html>
<html lang="de">
<head>
<meta charset="utf-8">
<title>Marta &amp; das Lindenwäldchen – Visitenkarte</title>
<link rel="stylesheet" href="https://fonts.googleapis.com/css2?family=Courier+Prime:wght@400;700&family=Dancing+Script:wght@400&display=swap">
<style>
  :root {
    --backdrop: #e9e9e9;
    --card: #dccfbc;
    --ink: #1c1a18;
    --rule: #2a2725;
  }
  * { margin: 0; padding: 0; box-sizing: border-box; }
  html, body {
    width: 1200px; height: 900px; overflow: hidden;
    background: var(--backdrop);
  }
  .canvas {
    width: 1200px; height: 900px;
    display: flex; align-items: center; justify-content: center;
  }
  .card {
    position: relative;
    width: 1050px; height: 600px;
    background: var(--card);
    color: var(--ink);
    box-shadow: 0 6px 18px rgba(0,0,0,0.15);
  }
  .tagline {
    position: absolute; left: 68px; right: 68px; top: 36px;
    display: flex; justify-content: space-between;
    font-family: "Courier Prime", monospace; font-weight: 700;
    font-size: 27px; letter-spacing: 0.32em;
  }
  .tagline span:last-child { letter-spacing: 0.32em; margin-right: -0.32em; }
  .rule {
    position: absolute; left: 68px; right: 64px; top: 87px;
    height: 3px; background: var(--rule); border-radius: 2px;
  }
  .title {
    position: absolute; left: 0; right: 0; top: 160px;
    text-align: center;
    font-family: "Dancing Script", cursive; font-weight: 400;
    font-size: 84px; line-height: 1;
  }
  .ellipsis {
    position: absolute; left: 0; right: 0; top: 258px;
    text-align: center;
    font-family: "Courier Prime", monospace; font-size: 26px; letter-spacing: 0.4em;
  }
  .subtitle {
    position: absolute; left: 0; right: 0; top: 310px;
    text-align: center;
    font-family: "Dancing Script", cursive;
    font-size: 56px; line-height: 1;
  }
  .address {
    position: absolute; left: 68px; top: 450px;
    font-family: "Courier Prime", monospace; font-size: 21px; line-height: 31px;
    letter-spacing: 0.06em;
  }
  .address .name { font-weight: 700; }
  .contact {
    position: absolute; left: 646px; top: 446px;
    font-family: "Courier Prime", monospace; font-size: 21px;
    letter-spacing: 0.06em;
  }
  .contact-row { display: flex; align-items: center; height: 32px; }
  .contact-row svg { width: 30px; height: 26px; margin-right: 16px; flex: none; }
  .contact-row svg * { fill: none; stroke: var(--ink); stroke-width: 1.4; }
</style>
</head>
<body>
<main class="canvas">
  <article class="card">
    <p class="tagline"><span>ENTSPANNEN</span><span>-</span><span>LOSLASSEN</span><span>-</span><span>AUFTANKEN</span></p>
    <div class="rule"></div>
    <h1 class="title">Marta &amp; das Lindenwäldchen</h1>
    <p class="ellipsis">...</p>
    <p class="subtitle">Urlaub an einem besonderen Ort</p>

    <address class="address">
      <span class="name">Marta Brecke</span><br>
      Grauer Pfad 7<br>
      18471 Alt Feldow
    </address>

    <div class="contact">
      <div class="contact-row">
        <svg viewBox="0 0 30 26" aria-label="Telefon"><rect x="10" y="1" width="11" height="23" rx="2"/><line x1="11" y1="19" x2="20" y2="19"/><circle cx="15.5" cy="21.5" r="0.8"/></svg>
      </div>
      <div class="contact-row">
        <svg viewBox="0 0 30 26" aria-label="E-Mail"><rect x="2" y="6" width="26" height="15" rx="1"/><polyline points="2,6 15,15 28,6"/></svg>
        <span>post@marta-brecke.de</span>
      </div>
      <div class="contact-row">
        <svg viewBox="0 0 30 26" aria-label="Web"><circle cx="14" cy="12" r="10"/><ellipse cx="14" cy="12" rx="4.5" ry="10"/><line x1="4" y1="12" x2="24" y2="12"/><line x1="6" y1="7" x2="22" y2="7"/><line x1="6" y1="17" x2="22" y2="17"/></svg>
        <span>www.lindenwaeldchen.net</span>
      </div>
    </div>
  </article>
</main>
</body>
</html>
```